依頼詳細
サイズはクレジットカードサイズ。nolpaによると国際規定は85.60 × 53.98 mmのようですがカード制作会社のサイトを見ていると86 × 54 mmが多いようです。ということで86 × 54 mmサイズで作成お願いします。

医院はこちら
http://sorahane-dental.jp/
http://hanagumo-implant.com/

医院の雰囲気などはサイトを参考になさって下さい。

電話番号は固定電話とフリーダイヤルの2つがありますが、フリーダイヤルのほう(0120-483-715)をお使い下さい。

記載項目
デザインの制限をかけたくないので、表面、裏面、に限定した記載項目は特に設定せずに依頼させて頂きます。全体に対して必要な項目を考えてみます。

【カードそのものの役割として】
医院名称は必須かと思います。ロゴが2種類(添付)あるのですが、使う使わないはお任せします。

カードのタイトルですが、「診察券」でいくかその他の名称(例えば「メンテナンスカード」とか)でいくか決めかねています。※医院名があれば無くても成立する?あくまで医療なので「VIPカード」みたいなタイトルは使いにくいですが、何かアイデアがあればデザインに反映させてご提案下さい。

【医院目線】
医院として、最低限「お名前」「カルテ番号」の2つの情報があれば業務は成り立ちます。表面でも裏面でも結構です。

【患者さん目線】
「電話番号」「受付時間」は必要かと思います。

「医院の場所」「診療日、休診日」は、カードが使われるシチュエーションを考えた場合、必要なのかどうか疑問です。デザイン優先で考えて頂き、「あった方がデザインしやすい」ようであれば使って下さい。
希望イメージ
シンプル 複雑
単色 カラフル
暗い 明るい
日常 高級
遊び心 厳粛
未来的 伝統的
女性的 男性的
希望する色
黒・ゴールド・プラチナ系
納品ファイル
• イラストレーター形式 (.ai)
補足説明
ロゴのaiファイルを添付します。
提案ありがとうございます。

これまで頂いた提案を院長が見て、「普段使っている診察券のデザインを保持しつつ、色合いを変更することでプレミアム感を出すのもいいかもしれませんね」という話が出てきました。

ということで、現在使っている診察券の裏表を添付ファイルとしてアップさせて頂きます。ファイルはスキャンしたものなのでベクター素材になっておりませんが、うまく使って頂ければと思います。

なお、「現在の診察券ベースの配色違い」のご提案の方が選定確率が高くなることはありません。1つのアイデアとして参考にして下さい。
医院のロゴが開かないという指摘を受けました。

対応策としてaiの保存バージョンを落としたもの(CS4バージョンで保存)と、編集機能を保持したpdfバージョンを添付してみます。開かない場合はこちらを試してみて下さい。
■ 選んだ理由

この作品が院長のセンスに一番近かったようです。

2次元ではなく実物を写真で撮影したような提案ということで、メージが湧きやすかったことも選定の要因かもしれません。

■ 提案者全員のお礼・コメント

この案件のために時間をとっていただきありがとうございました。沢山の素敵なご提案感謝しております。

選定はだいぶ悩みましたが、最終的に好みの問題で決めさせて頂いた感じです。

また機会があればよろしくお願いします。

```html
<!DOCTYPE html>
<html lang="ja">
<head>
<meta charset="utf-8">
<title>Hanagumo Implant Clinic — members card proof</title>
<link rel="stylesheet" href="https://fonts.googleapis.com/css2?family=Marcellus&family=Cormorant+Garamond:ital,wght@1,500&family=Shippori+Mincho:wght@600&family=Noto+Sans+JP:wght@400;700&display=swap">
<style>
  :root{
    --paper:#ffffff;
    --ink:#222222;
    --gold:#a67b45;
    --gold-dark:#7d5a2e;
    --cream:#f4ead6;
    --white:#ffffff;
    --clover:#e6b53a;
    --mark:#555555;
  }
  *{margin:0;padding:0;box-sizing:border-box}
  html,body{width:735px;height:1200px;overflow:hidden;background:var(--paper)}
  body{position:relative;font-family:"Noto Sans JP",sans-serif;color:var(--ink)}
  .crop-marks{position:absolute;left:0;top:0}
  .ink-spec{position:absolute;left:38px;display:flex;align-items:center;gap:10px;font-size:13px;color:var(--ink)}
  .ink-spec .swatch{width:32px;height:30px;background:var(--gold)}
  .ink-spec.front-spec{top:96px}
  .ink-spec.back-spec{top:656px}

  .card{position:absolute;left:160px;width:415px;height:262px;border-radius:16px;background:var(--gold)}
  .card.front{top:220px}
  .card.back{top:785px}

  /* front */
  .front .frame{position:absolute;inset:9px;border:1.5px solid var(--cream);border-radius:11px}
  .front .clinic-title{position:absolute;top:20px;left:0;right:0;text-align:center;font-family:"Marcellus",serif;font-size:24px;color:var(--white);letter-spacing:.5px}
  .front .ornament{position:absolute;top:28px;width:32px;height:12px;border-radius:6px;background:var(--cream);opacity:.85}
  .front .ornament.left{left:24px}
  .front .ornament.right{right:24px}
  .front .banner{position:absolute;left:0;top:0}
  .front .label{position:absolute;font-family:"Cormorant Garamond",serif;font-style:italic;font-size:11px;color:var(--gold-dark)}
  .front .label.name-label{left:66px;top:78px}
  .front .label.number-label{left:210px;top:131px}
  .front .member-name{position:absolute;left:142px;top:84px;font-family:"Shippori Mincho",serif;font-size:34px;letter-spacing:3px;color:var(--ink)}
  .front .honorific{position:absolute;left:334px;top:108px;font-family:"Shippori Mincho",serif;font-size:11px}
  .front .member-number{position:absolute;left:290px;top:126px;font-family:"Noto Sans JP",sans-serif;font-size:18px;color:var(--ink)}
  .front .clover{position:absolute;left:30px;top:148px;width:58px;height:60px;border-radius:50%;background:radial-gradient(circle,var(--clover),#d39a23)}
  .front .rule{position:absolute;left:80px;right:80px;top:198px;height:1px;background:var(--cream)}
  .front .card-title{position:absolute;left:0;right:0;top:204px;text-align:center;font-family:"Marcellus",serif;font-size:22px;color:var(--white)}

  /* back */
  .back .panel{position:absolute;inset:12px;background:var(--white);border-radius:10px}
  .back .brand{position:absolute;left:0;right:0;top:22px;display:flex;flex-direction:column;align-items:center;gap:4px}
  .back .brand .dot{width:40px;height:40px;border-radius:50%;background:var(--gold)}
  .back .brand .brand-name{font-size:10px;color:var(--gold-dark);font-weight:700;letter-spacing:1px}
  .back .inquiry{position:absolute;left:110px;top:100px;font-size:10px;color:var(--ink)}
  .back .phone{position:absolute;left:110px;top:112px;font-size:30px;letter-spacing:1px;color:var(--ink);font-weight:400}
  .back .hours{position:absolute;left:110px;top:152px;font-size:13px;color:var(--ink);display:flex;align-items:center;gap:8px}
  .back .hours small{font-size:8px}
  .back .clinic-name{position:absolute;left:20px;right:20px;top:196px;text-align:center;font-size:16px;font-weight:700;color:var(--gold);border-top:1px solid #e3d3b5;padding-top:6px}
</style>
</head>
<body>

<svg class="crop-marks" width="735" height="1200" viewBox="0 0 735 1200" fill="none" stroke="var(--mark)" stroke-width="0.8" aria-hidden="true">
  <g>
    <path d="M100 220H150M100 208H150M160 160V210M148 160V210"/>
    <path d="M635 220H585M635 208H585M575 160V210M587 160V210"/>
    <path d="M100 482H150M100 494H150M160 542V492M148 542V492"/>
    <path d="M635 482H585M635 494H585M575 542V492M587 542V492"/>
    <path d="M367 160V205M350 185H384M100 351H145M82 340V362M635 351H590M653 340V362M367 542V497M350 520H384"/>
  </g>
  <g transform="translate(0 565)">
    <path d="M100 220H150M100 208H150M160 160V210M148 160V210"/>
    <path d="M635 220H585M635 208H585M575 160V210M587 160V210"/>
    <path d="M100 482H150M100 494H150M160 542V492M148 542V492"/>
    <path d="M635 482H585M635 494H585M575 542V492M587 542V492"/>
    <path d="M367 160V205M350 185H384M100 351H145M82 340V362M635 351H590M653 340V362M367 542V497M350 520H384"/>
  </g>
</svg>

<div class="ink-spec front-spec"><span>4C +</span><span class="swatch"></span><span>特色：金（DIC619）</span></div>

<section class="card front">
  <div class="frame"></div>
  <span class="ornament left" role="img" aria-label="Scroll ornament"></span>
  <h1 class="clinic-title">Hanagumo Implant Clinic</h1>
  <span class="ornament right" role="img" aria-label="Scroll ornament"></span>
  <svg class="banner" width="415" height="262" viewBox="0 0 415 262" aria-hidden="true">
    <path d="M40 72H375L390 108L375 144H40L55 108Z" fill="var(--white)"/>
    <path d="M62 126H360" stroke="var(--gold)" stroke-width="1"/>
  </svg>
  <span class="label name-label">members name</span>
  <span class="member-name">空羽太郎</span>
  <span class="honorific">様</span>
  <span class="label number-label">members number</span>
  <span class="member-number">318-05267</span>
  <div class="clover" role="img" aria-label="Four-leaf clover illustration"></div>
  <div class="rule"></div>
  <p class="card-title">members card</p>
</section>

<div class="ink-spec back-spec"><span>4C +</span><span class="swatch"></span><span>特色：金（DIC619）</span></div>

<section class="card back">
  <div class="panel"></div>
  <div class="brand"><span class="dot"></span><span class="brand-name">HANAGUMO</span></div>
  <p class="inquiry">お問い合わせ　フリーダイアル</p>
  <p class="phone">0120-483-715</p>
  <p class="hours"><small>受付時間</small>8：40 ～ 19：15</p>
  <p class="clinic-name">花雲インプラントクリニック　そらはね歯科</p>
</section>

</body>
</html>
```